Hawaiian Body Care Product Catalog for Wholesaling

Design a multi page catalog for a Hawaiian body care brand. There are about 6 different types of products (for example, soaps, lotions, lip balms) and we have about 50 products.

Catalog size: 5.5" x 8.5"

Please visit our website at www.corallumecare.example to get an idea of our product line and aesthetic. We would like to focus on the fun tropical fruit. This catalog to for sales reps to show retailers - so it's a wholesale catalog.

Target Market(s)

Retailers as were are wholesaling to them.

Industry/Entity Type

Beauty

Font styles to use
Sans Serif

Colors

Designer to choose colors to be used in the design.

Requirements
Must have
• Images of tropical fruit - we have a lot of stock images that I was unable to file transfer because it said they were too wide.
• Hi Res images for print.
Nice to have
• Images of each product per type of product. Descriptions of the products found on website. SKU under the images of each product. no pricing, just sku number. Playful images of tropical fruit, flowers and Hawaii. Somewhere we need to explain that we are donating 5% net profits to protect Hawaiian Wildlife, so maybe a page dedicated to that with an image of Hawaiian Wildlife.

```html
<!DOCTYPE html>
<html lang="en">
<head>
<meta charset="utf-8">
<title>Moisturizers – Body Lotion Catalog Spread</title>
<link href="https://fonts.googleapis.com/css2?family=Jost:wght@400;500;700&family=Open+Sans:wght@400;600&display=swap" rel="stylesheet">
<style>
  :root{
    --backdrop:#ece9e4;
    --paper:#ffffff;
    --ink:#3a3a3a;
    --ink-soft:#555;
    --accent:#e0196b;
    --teal-deep:#1d8fb0;
    --teal:#2bb7d3;
    --teal-light:#5fd3e6;
  }
  *{box-sizing:border-box;margin:0;padding:0}
  html,body{width:1200px;height:800px;overflow:hidden;background:var(--backdrop)}
  .spread{
    position:absolute;left:20px;top:186px;width:1160px;height:428px;
    display:flex;box-shadow:0 6px 18px rgba(0,0,0,.18);
  }
  .page{position:relative;width:580px;height:428px;background:var(--paper);overflow:hidden}
  .page--left{background:linear-gradient(to right,var(--paper) 88%,#e6e6e6 100%)}
  .page--right{background:linear-gradient(to left,var(--paper) 88%,#e6e6e6 100%)}

  .hero{
    position:absolute;left:0;top:0;width:274px;height:428px;
    background:
      radial-gradient(ellipse at 75% 40%,rgba(125,166,63,.55) 0,rgba(125,166,63,.25) 30%,transparent 60%),
      linear-gradient(135deg,var(--teal-deep),var(--teal) 45%,var(--teal-light));
  }
  .hero__text{position:absolute;left:30px;top:178px;width:228px;color:#fff;font-family:"Jost",sans-serif}
  .hero__kicker{font-size:23px;font-weight:400;letter-spacing:.3px;line-height:1}
  .hero__title{font-size:24px;font-weight:700;line-height:1.05;margin-bottom:16px}
  .hero__copy{font-family:"Open Sans",sans-serif;font-size:7.4px;line-height:1.45;margin-bottom:10px}

  .product{position:absolute;width:250px;font-family:"Open Sans",sans-serif;color:var(--ink-soft)}
  .product__type{font-family:"Jost",sans-serif;font-size:7.4px;color:var(--accent);text-transform:uppercase;line-height:1.1;white-space:nowrap}
  .product__name{font-family:"Jost",sans-serif;font-weight:700;font-size:7px;color:var(--accent);text-transform:uppercase;line-height:1.2;margin-bottom:4px;white-space:nowrap}
  .product__body{display:flex;gap:20px}
  .product__image{flex:0 0 62px;height:84px;border-radius:4px;
    background:radial-gradient(ellipse at 45% 50%,#f2d6df 0,#f7eef1 45%,transparent 70%)}
  .product__image--amber{background:radial-gradient(ellipse at 50% 50%,#d9a07a 0,#eed9c9 40%,transparent 70%)}
  .product__info{flex:1;font-size:5.3px;line-height:1.3}
  .product__sku{font-weight:600;margin-bottom:5px}
  .product__info p{margin-bottom:4px}

  .footer{
    position:absolute;left:0;bottom:0;width:580px;height:32px;background:var(--accent);
    display:flex;align-items:center;justify-content:space-between;padding:0 22px 0 30px;
    font-family:"Open Sans",sans-serif;color:#fff;font-size:9px;
  }
  .footer__page{font-family:"Jost",sans-serif;font-size:12px}
</style>
</head>
<body>
<div class="spread">
  <section class="page page--left">
    <div class="hero" role="img" aria-label="Palm fronds on a bright turquoise background"></div>
    <div class="hero__text">
      <div class="hero__kicker">MOISTURIZERS</div>
      <div class="hero__title">BODY LOTION</div>
      <p class="hero__copy">Pamper your skin with moisturizing Coral Lume Care Co. Hawaiian Body Lotion loaded with herbs like Chamomile, Aloe, Calendula, Eyebright, Green Tea and Wild Geranium for delux skin conditioning. It is really yummy!</p>
      <p class="hero__copy">This delightful lotion absorbs right into the skin without leaving a greasy feeling yet provides the glide of a deep penetrating moisturizer. It conditions your skin while it moisturizes and softens and will stay on even through hand washing.</p>
    </div>

    <article class="product" style="left:305px;top:38px">
      <div class="product__type">Body Lotion</div>
      <div class="product__name">Awapuhi with Aloe, Avocado Oil, Cucumber &amp; Vitamin E</div>
      <div class="product__body">
        <div class="product__image" role="img" aria-label="Awapuhi body lotion bottle with pink hibiscus"></div>
        <div class="product__info">
          <div class="product__sku">SKU : -</div>
          <p>Paraben-free Awapuhi Body Lotion with Aloe Vera, Green Tea antioxidants and tropical Avocado Oil which absorbs quickly to help replenish and protect skin against dehydration for a soft, healthy, luminous complexion.</p>
          <p>Formulated with extracts of chamomile, cucumber and gotu kola, blended with golden jojoba oil and vitamin E for superior hydration.</p>
          <p>- Perfect for all skin types, pH balanced.<br>- 98% Natural | 70% Organic | 100% Vegan.</p>
        </div>
      </div>
    </article>

    <article class="product" style="left:305px;top:156px">
      <div class="product__type">Body Lotion</div>
      <div class="product__name">Coconut with Aloe, Avocado Oil, Cucumber &amp; Vitamin E</div>
      <div class="product__body">
        <div class="product__image" role="img" aria-label="Coconut body lotion bottle with pink hibiscus"></div>
        <div class="product__info">
          <div class="product__sku">SKU : -</div>
          <p>Paraben-free Coconut Body Lotion with Aloe Vera, Green Tea antioxidants and tropical Avocado Oil which absorbs quickly to help replenish and protect skin against dehydration for a soft, healthy, luminous complexion.</p>
          <p>Formulated with extracts of chamomile, cucumber and gotu kola, blended with golden jojoba oil and vitamin E for superior hydration.</p>
          <p>- Perfect for all skin types, pH balanced.<br>- 98% Natural | 70% Organic | 100% Vegan.</p>
        </div>
      </div>
    </article>

    <article class="product" style="left:305px;top:274px">
      <div class="product__type">Body Lotion</div>
      <div class="product__name">Mango with Aloe, Avocado Oil, Cucumber &amp; Vitamin E</div>
      <div class="product__body">
        <div class="product__image" role="img" aria-label="Mango body lotion bottle with pink hibiscus"></div>
        <div class="product__info">
          <div class="product__sku">SKU : -</div>
          <p>Paraben-free Mango Body Lotion with Aloe Vera, Green Tea antioxidants and tropical Avocado Oil which absorbs quickly to help replenish and protect skin against dehydration for a soft, healthy, luminous complexion.</p>
          <p>Formulated with extracts of chamomile, cucumber and gotu kola, blended with golden jojoba oil and vitamin E for superior hydration.</p>
          <p>- Perfect for all skin types, pH balanced.<br>- 98% Natural | 70% Organic | 100% Vegan.</p>
        </div>
      </div>
    </article>
  </section>

  <section class="page page--right">
    <article class="product" style="left:33px;top:40px">
      <div class="product__type">Body Lotion</div>
      <div class="product__name">Pikake with Aloe, Avocado Oil, Cucumber &amp; Vitamin E</div>
      <div class="product__body">
        <div class="product__image" role="img" aria-label="Pikake body lotion bottle with pink hibiscus"></div>
        <div class="product__info">
          <div class="product__sku">SKU : -</div>
          <p>Paraben-free Pikake Body Lotion with Aloe Vera, Green Tea antioxidants and tropical Avocado Oil which absorbs quickly to help replenish and protect skin against dehydration for a soft, healthy, luminous complexion.</p>
          <p>Formulated with extracts of chamomile, cucumber and gotu kola, blended with golden jojoba oil and vitamin E for superior hydration.</p>
          <p>- Perfect for all skin types, pH balanced.<br>- 98% Natural | 70% Organic | 100% Vegan.</p>
        </div>
      </div>
    </article>

    <article class="product" style="left:33px;top:158px">
      <div class="product__type">Body Lotion</div>
      <div class="product__name">Plumeria with Aloe, Avocado Oil, Cucumber &amp; Vitamin E</div>
      <div class="product__body">
        <div class="product__image" role="img" aria-label="Plumeria body lotion bottle with pink hibiscus"></div>
        <div class="product__info">
          <div class="product__sku">SKU : -</div>
          <p>Paraben-free Plumeria Body Lotion with Aloe Vera, Green Tea antioxidants and tropical Avocado Oil which absorbs quickly to help replenish and protect skin against dehydration for a soft, healthy, luminous complexion.</p>
          <p>Formulated with extracts of chamomile, cucumber and gotu kola, blended with golden jojoba oil and vitamin E for superior hydration.</p>
          <p>- Perfect for all skin types, pH balanced.<br>- 98% Natural | 70% Organic | 100% Vegan.</p>
        </div>
      </div>
    </article>

    <article class="product" style="left:33px;top:277px">
      <div class="product__type">Hawaiian Aromatherapy Body Lotion</div>
      <div class="product__name">Coconut Milk</div>
      <div class="product__body">
        <div class="product__image product__image--amber" role="img" aria-label="Coconut milk aromatherapy lotion pump bottle"></div>
        <div class="product__info">
          <div class="product__sku">SKU : -</div>
          <p>Hawaiian Aromatherapy Body Lotion made with essential oils. 10% of net profits go towards protecting wildlife in Hawaii.</p>
        </div>
      </div>
    </article>

    <article class="product" style="left:308px;top:40px">
      <div class="product__type">Hawaiian Aromatherapy Body Lotion</div>
      <div class="product__name">Hibiscus Passion</div>
      <div class="product__body">
        <div class="product__image product__image--amber" role="img" aria-label="Hibiscus passion aromatherapy lotion pump bottle"></div>
        <div class="product__info">
          <div class="product__sku">SKU : -</div>
          <p>Hawaiian Aromatherapy Body Lotion made with essential oils. 10% of net profits go towards protecting wildlife in Hawaii.</p>
        </div>
      </div>
    </article>

    <article class="product" style="left:308px;top:158px">
      <div class="product__type">Hawaiian Aromatherapy Body Lotion</div>
      <div class="product__name">Honey Almond</div>
      <div class="product__body">
        <div class="product__image product__image--amber" role="img" aria-label="Honey almond aromatherapy lotion pump bottle"></div>
        <div class="product__info">
          <div class="product__sku">SKU : -</div>
          <p>Hawaiian Aromatherapy Body Lotion made with essential oils. 10% of net profits go towards protecting wildlife in Hawaii.</p>
        </div>
      </div>
    </article>

    <article class="product" style="left:308px;top:277px">
      <div class="product__type">Hawaiian Aromatherapy Body Lotion</div>
      <div class="product__name">Lavender Fields</div>
      <div class="product__body">
        <div class="product__image product__image--amber" role="img" aria-label="Lavender fields aromatherapy lotion pump bottle"></div>
        <div class="product__info">
          <div class="product__sku">SKU : -</div>
          <p>Hawaiian Aromatherapy Body Lotion made with essential oils. 10% of net profits go towards protecting wildlife in Hawaii.</p>
        </div>
      </div>
    </article>

    <footer class="footer">
      <span>www.corallumecare.example &nbsp;|&nbsp; info@corallumecare.example</span>
      <span class="footer__page">14</span>
    </footer>
  </section>
</div>
</body>
</html>
```